Extremely Professional Lawyer needs letterhead for new boutique real estate law firm

I need letterhead for my new solo practice law firm. I practiced as a partner in a huge global law firm for years. Now I am starting a solo firm where I will deliver very high-quality legal services that are real-estate focused. The idea is that my practice will be very focused but that the services will be at the quality level provided by partners at high-profile law firms. The name of my law firm will be Brenner Law Group, LLC. For now, I am the only lawyer. I expect to negotiate and draft house sale/purchase contracts and close house deals. Eventually, I would like to do small-scale development deals for developer clients, a specialty of mine.

Industry/Entity Type

Boutique

```html
<!DOCTYPE html>
<html lang="en">
<head>
<meta charset="UTF-8">
<title>Brenner Law Group, LLC — Letterhead</title>
<link href="https://fonts.googleapis.com/css2?family=Josefin+Slab:wght@400;700&family=Parisienne&display=swap" rel="stylesheet">
<style>
  :root {
    --ink-green: #0c4a2c;
    --rule-green: #3f6b55;
    --mist-green: #cdf9d0;
    --paper: #ffffff;
  }
  html, body {
    margin: 0;
    padding: 0;
    overflow: hidden;
    background: var(--paper);
  }
  .letterhead {
    position: relative;
    width: 847px;
    height: 1200px;
    background: var(--paper);
    overflow: hidden;
  }
  .tagline {
    position: absolute;
    left: 34px;
    top: 119px;
    font-family: "Parisienne", cursive;
    font-size: 17px;
    line-height: 24px;
    color: var(--ink-green);
    white-space: nowrap;
  }
  .tagline-rule {
    position: absolute;
    left: 187px;
    top: 139px;
    width: 451px;
    height: 1px;
    background: var(--rule-green);
  }
  .firm-name {
    position: absolute;
    right: 35px;
    top: 86px;
    margin: 0;
    font-family: "Josefin Slab", serif;
    font-weight: 700;
    font-size: 23px;
    line-height: 26px;
    letter-spacing: 0.5px;
    text-transform: uppercase;
    color: var(--ink-green);
    text-align: right;
    white-space: nowrap;
  }
  .firm-name span {
    display: block;
  }
  .firm-name-backdrop {
    position: absolute;
    left: 0;
    right: 0;
    top: 520px;
    font-family: "Josefin Slab", serif;
    font-weight: 700;
    font-size: 62px;
    line-height: 70px;
    letter-spacing: 1px;
    text-transform: uppercase;
    color: var(--mist-green);
    text-align: center;
    white-space: nowrap;
  }
  .firm-name-backdrop span {
    display: block;
  }
  .footer-rule {
    position: absolute;
    left: 162px;
    top: 1128px;
    width: 524px;
    height: 1px;
    background: var(--rule-green);
  }
  .contact-line {
    position: absolute;
    left: 0;
    right: 0;
    top: 1134px;
    font-family: "Josefin Slab", serif;
    font-weight: 400;
    font-size: 16px;
    line-height: 20px;
    color: var(--ink-green);
    text-align: center;
    white-space: nowrap;
  }
</style>
</head>
<body>
  <main class="letterhead">
    <header>
      <div class="tagline">Your tag line goes here</div>
      <div class="tagline-rule"></div>
      <h1 class="firm-name"><span>Brenner Law</span><span>Group, LLC.</span></h1>
    </header>

    <div class="firm-name-backdrop" aria-hidden="true"><span>Brenner Law</span><span>Group, LLC.</span></div>

    <footer>
      <div class="footer-rule"></div>
      <div class="contact-line">Office address goes here | Telephone, fax, mobile goes here | email address here | company website address here</div>
    </footer>
  </main>
</body>
</html>
```